Website redesign

Looking to redesign our existing website. (hire4ward.com.au)
New design needs to be bright, fun and have an easy flowing.
The website needs to be design with call to action.

Some examples of other websites:
brightdesk.com
lendnest.com.au

We are happy with the content of our existing website.

Target Market(s)

other businesses

Industry/Entity Type

Business Service

Number of Pages Required

5+ page

Requirements
Must have
• Theme redesign
Cool animation similar to brightdesk.com

```html
<!DOCTYPE html>
<html lang="en">
<head>
<meta charset="utf-8">
<title>Hire 4 Ward – Outsourcing</title>
<link href="https://fonts.googleapis.com/css2?family=Lato:wght@400;700;900&display=swap" rel="stylesheet">
<style>
:root{
  --hero:#0db1e8;
  --hero-soft:#2bb9ec;
  --hero-deep:#109fd6;
  --accent:#1aa3dd;
  --icon:#4a9fdf;
  --ink:#111820;
  --body:#555b63;
  --muted:#8a9099;
  --panel:#eff3f7;
  --line:#d7dde4;
  --navy:#0f1c2e;
  --white:#ffffff;
}
*{margin:0;padding:0;box-sizing:border-box}
html,body{width:1200px;height:4135px;overflow:hidden}
body{font-family:'Lato',sans-serif;color:var(--ink);background:var(--white);position:relative}
.abs{position:absolute}
section,header,footer{position:absolute;left:0;width:1200px}

/* header */
.site-header{top:0;height:106px;background:var(--white)}
.brand{left:109px;top:30px;display:flex;align-items:center;gap:10px;font-size:24px;font-weight:700;letter-spacing:.5px;color:var(--ink)}
.brand-dot{width:26px;height:26px;border-radius:50%;background:var(--accent)}
.callus{right:228px;top:20px;font-size:16px;display:flex;align-items:center;gap:7px}
.callus b{font-size:21px;font-weight:700;margin-left:4px}
.login{left:994px;top:10px;width:96px;height:46px;background:var(--accent);color:var(--white);font-size:16px;display:flex;align-items:center;justify-content:center;gap:6px;border-radius:2px}
.nav{top:68px;right:110px;display:flex;gap:42px;font-size:17px}
.nav a{color:var(--ink);text-decoration:none;position:relative}
.nav a.active{color:var(--accent)}
.nav a.active::after{content:"";position:absolute;left:50%;top:28px;width:16px;height:6px;margin-left:-8px;border-radius:3px;background:var(--accent)}

/* hero */
.hero{top:106px;height:594px;background:var(--hero);overflow:hidden}
.hero-halo{left:455px;top:-30px;width:780px;height:780px;border-radius:50%;background:var(--hero-soft)}
.hero-art{left:640px;top:45px;width:440px;height:440px;border-radius:50%;background:radial-gradient(circle,#ffffff 0 18%,var(--hero-deep) 19% 100%)}
.hero h1{left:107px;top:110px;font-size:86px;font-weight:900;color:var(--white);letter-spacing:-1px}
.hero p{left:109px;top:226px;font-size:32px;line-height:46px;color:var(--white)}
.cta{left:109px;top:351px;width:228px;height:66px;background:var(--white);color:var(--ink);font-weight:900;font-size:22px;display:flex;align-items:center;justify-content:center}

/* shared */
.mark{left:575px;width:50px;height:50px;border-radius:50%;border:5px solid var(--icon)}
.section-title{left:0;width:1200px;text-align:center;font-size:44px;font-weight:700;color:var(--ink);line-height:57px}
.lede{left:0;width:1200px;text-align:center;font-size:15px;line-height:30px;color:var(--body)}

/* welcome */
.welcome{top:700px;height:750px}
.video{left:248px;top:297px;width:703px;height:381px;background:linear-gradient(110deg,#1d7fb8,#3aa7de 50%,#1a4f7a);box-shadow:0 4px 10px rgba(0,0,0,.2)}
.play{left:560px;top:449px;width:80px;height:80px}

/* process */
.process{top:1450px;height:613px;background:var(--panel);overflow:hidden}
.process svg{position:absolute;left:0;top:0}

/* services */
.services{top:2063px;height:677px}
.service{width:472px;height:155px;border:3px solid var(--line);display:flex;align-items:center;padding-left:32px;gap:36px;font-size:21px;line-height:34px;color:#333}
.service-art{flex:none;width:95px;height:95px;border-radius:8px;background:linear-gradient(135deg,#7fc6ec,#f3b24c)}

/* why */
.why{top:2740px;height:740px;background:var(--panel)}
.why-grid{left:109px;top:260px;width:982px;height:440px}
.cell{position:absolute;width:327px;text-align:center;font-size:20px;line-height:32px;color:#444}
.cell svg{display:block;margin:0 auto 20px}

/* contact */
.contact{top:3480px;height:570px;background:var(--navy);color:var(--white);overflow:hidden}
.contact-halo{left:380px;top:150px;width:440px;height:440px;border-radius:50%;border:60px solid #15263b}
.contact .section-title{color:var(--white)}
.col-title{font-size:22px}
.field{height:44px;border:1px solid #5c6878;border-radius:3px;font-size:14px;padding:15px 0 0 15px;color:#d5dae0}
.submit{left:617px;top:475px;width:96px;height:42px;background:var(--accent);font-size:15px;font-weight:700;display:flex;align-items:center;justify-content:center;border-radius:2px}
.info-row{left:778px;display:flex;align-items:center;gap:15px;font-size:15px}
.ring{width:34px;height:34px;border-radius:50%;border:1.5px solid #c8ced6;display:flex;align-items:center;justify-content:center}

/* footer */
.site-footer{top:4050px;height:85px;background:var(--white)}
.copyright{left:0;width:1200px;top:37px;text-align:center;font-size:15px;color:var(--muted)}
</style>
</head>
<body>

<header class="site-header">
  <div class="abs brand"><span class="brand-dot"></span>HIRE 4 WARD</div>
  <div class="abs callus">
    <svg width="14" height="14" viewBox="0 0 24 24"><path fill="#1aa3dd" d="M6.6 10.8a15 15 0 006.6 6.6l2.2-2.2c.3-.3.7-.4 1-.2 1.1.4 2.3.6 3.6.6.6 0 1 .4 1 1V20c0 .6-.4 1-1 1A17 17 0 013 4c0-.6.4-1 1-1h3.5c.6 0 1 .4 1 1 0 1.3.2 2.5.6 3.6.1.3 0 .7-.2 1z"/></svg>
    CALL US <b>07 3000 4821</b>
  </div>
  <div class="abs login">
    <svg width="12" height="14" viewBox="0 0 12 14"><rect x="1" y="6" width="10" height="8" rx="1" fill="#fff"/><path d="M3 6V4a3 3 0 016 0v2" stroke="#fff" stroke-width="2" fill="none"/></svg>
    LOGIN
  </div>
  <nav class="abs nav">
    <a class="active">HOME</a><a>OUR STORY</a><a>TIPS AND TRICKS</a><a>FAQ</a><a>CONTACT US</a>
  </nav>
</header>

<section class="hero">
  <div class="abs hero-halo"></div>
  <div class="abs hero-art" role="img" aria-label="Illustration of a clock circled by arrows"></div>
  <h1 class="abs">OUTSOURCING</h1>
  <p class="abs">A big word that means big things<br>for your business.</p>
  <div class="abs cta">GET A QUOTE</div>
</section>

<section class="welcome">
  <div class="abs mark" style="top:40px"></div>
  <h2 class="abs section-title" style="top:105px">WELCOME TO HIRE 4 WARD</h2>
  <p class="abs lede" style="top:178px">Virtual Assistants are the superheroes of the modern office. They can do everything your team<br>can do on a computer at a fraction of the price! (Well, maybe not high five you when you've had a win,<br>but a virtual high five is definitely on the table!)</p>
  <div class="abs video" role="img" aria-label="Video still of two team members introducing the company"></div>
  <svg class="abs play" viewBox="0 0 80 80"><circle cx="40" cy="40" r="37" fill="none" stroke="#fff" stroke-width="4"/><path d="M32 26l22 14-22 14z" fill="#fff"/></svg>
</section>

<section class="process">
  <div class="abs mark" style="top:40px"></div>
  <h2 class="abs section-title" style="top:105px">OUR PROCESS</h2>
  <svg width="1200" height="613" viewBox="0 0 1200 613" font-family="Lato, sans-serif">
    <circle cx="600" cy="580" r="255" fill="#fff" stroke="#d9dee5" stroke-width="3"/>
    <text x="600" y="533" text-anchor="middle" font-size="80" font-weight="900" fill="#111820">H4W</text>
    <g fill="#4a9fdf">
      <circle cx="600" cy="328" r="51"/>
      <circle cx="446" cy="383" r="51"/>
      <circle cx="755" cy="383" r="51"/>
      <circle cx="360" cy="511" r="51"/>
      <circle cx="845" cy="511" r="51"/>
    </g>
    <g stroke="#fff" stroke-width="4" fill="none" stroke-linecap="round">
      <circle cx="597" cy="325" r="11"/><path d="M605 333l9 9"/>
      <circle cx="446" cy="376" r="7"/><circle cx="433" cy="381" r="5"/><circle cx="459" cy="381" r="5"/><path d="M434 396a12 9 0 0124 0"/>
      <circle cx="750" cy="388" r="8"/><circle cx="766" cy="374" r="5"/><circle cx="766" cy="394" r="4"/>
      <rect x="346" y="499" width="22" height="22" rx="3"/><path d="M360 515l14-14"/>
      <circle cx="845" cy="511" r="16"/><path d="M838 516a9 7 0 0014 0"/>
    </g>
    <g fill="#111820" font-size="16">
      <text x="600" y="203" text-anchor="middle" fill="#777" font-size="14">STEP 3</text>
      <text x="600" y="228" text-anchor="middle">Conducting the Final Interview</text>
      <text x="600" y="257" text-anchor="middle" fill="#4a9fdf" font-size="15">READ MORE</text>

      <text x="357" y="313" text-anchor="end" fill="#777" font-size="14">STEP 2</text>
      <text x="357" y="340" text-anchor="end">Endorsing the Shortlisted</text>
      <text x="357" y="366" text-anchor="end">Candidates</text>
      <text x="357" y="400" text-anchor="end" fill="#4a9fdf" font-size="15">READ MORE</text>

      <text x="838" y="313" fill="#777" font-size="14">STEP 4</text>
      <text x="838" y="340">Setting up the Tools</text>
      <text x="838" y="371" fill="#4a9fdf" font-size="15">READ MORE</text>

      <text x="297" y="483" text-anchor="end" fill="#777" font-size="14">STEP 1</text>
      <text x="297" y="510" text-anchor="end">Provide Your Preferred</text>
      <text x="297" y="536" text-anchor="end">Qualifications</text>
      <text x="297" y="569" text-anchor="end" fill="#4a9fdf" font-size="15">READ MORE</text>

      <text x="915" y="483" fill="#777" font-size="14">STEP 5</text>
      <text x="915" y="510">Your Magical Journey</text>
      <text x="915" y="536">Begins</text>
      <text x="915" y="569" fill="#4a9fdf" font-size="15">READ MORE</text>
    </g>
  </svg>
  <div class="abs mark" style="top:40px"></div>
</section>

<section class="services">
  <div class="abs mark" style="top:40px"></div>
  <h2 class="abs section-title" style="top:105px">OUR SERVICES</h2>
  <p class="abs lede" style="top:180px">We'll help you save tens (or even hundreds!) of thousands of dollars per year.<br>But what do WE actually do? GLAD YOU ASKED!</p>
  <div class="abs service" style="left:111px;top:277px"><div class="service-art" role="img" aria-label="Illustration of an assistant at a laptop"></div>We recruit Virtual Assistants<br>(a.k.a office legends!)</div>
  <div class="abs service" style="left:611px;top:277px"><div class="service-art" role="img" aria-label="Illustration of a support agent with gears"></div>Provide the tech support for<br>these superheroes!</div>
  <div class="abs service" style="left:111px;top:459px"><div class="service-art" role="img" aria-label="Illustration of a phone with gears"></div>Set up the phone system<br>(their own Bat Phone!)</div>
  <div class="abs service" style="left:611px;top:459px"><div class="service-art" role="img" aria-label="Illustration of a stopwatch and gears"></div>We manage Virtual Assistants<br>and keep them in tip-top<br>shape!</div>
</section>

<section class="why">
  <div class="abs mark" style="top:43px"></div>
  <h2 class="abs section-title" style="top:105px">WHY ARE WE YOUR NEW<br>BEST OUTSOURCING FRIEND?</h2>
  <div class="abs why-grid">
    <svg class="abs" style="left:0;top:0" width="982" height="440"><g stroke="#cfd5dc" stroke-width="1.5"><line x1="327" y1="0" x2="327" y2="440"/><line x1="654" y1="0" x2="654" y2="440"/><line x1="0" y1="207" x2="982" y2="207"/></g></svg>
    <div class="cell" style="left:0;top:45px"><svg width="40" height="44" viewBox="0 0 40 44"><circle cx="20" cy="12" r="10" fill="#4a9fdf"/><path d="M2 44a18 16 0 0136 0z" fill="#4a9fdf"/></svg>Your Own<br>Virtual Assistant</div>
    <div class="cell" style="left:327px;top:45px"><svg width="40" height="46" viewBox="0 0 40 46"><path d="M2 0h26l10 10v36H2z" fill="#4a9fdf"/><g stroke="#fff" stroke-width="3"><line x1="10" y1="22" x2="30" y2="22"/><line x1="10" y1="30" x2="30" y2="30"/><line x1="10" y1="38" x2="30" y2="38"/></g></svg>One Invoice<br>Per Month</div>
    <div class="cell" style="left:654px;top:45px"><svg width="42" height="46" viewBox="0 0 42 46"><rect x="1.5" y="1.5" width="39" height="43" rx="3" fill="none" stroke="#4a9fdf" stroke-width="3"/><rect x="7" y="7" width="28" height="8" fill="#4a9fdf"/><g fill="#4a9fdf"><rect x="7" y="20" width="6" height="5"/><rect x="18" y="20" width="6" height="5"/><rect x="29" y="20" width="6" height="5"/><rect x="7" y="29" width="6" height="5"/><rect x="18" y="29" width="6" height="5"/><rect x="29" y="29" width="6" height="5"/><rect x="7" y="37" width="6" height="4"/><rect x="18" y="37" width="6" height="4"/><rect x="29" y="37" width="6" height="4"/></g></svg>No Super or<br>TAX</div>
    <div class="cell" style="left:0;top:245px"><svg width="48" height="40" viewBox="0 0 48 40"><path d="M16 6V2h16v4" stroke="#4a9fdf" stroke-width="3" fill="none"/><rect x="0" y="7" width="48" height="33" rx="4" fill="#4a9fdf"/><g stroke="#fff" stroke-width="2"><line x1="10" y1="7" x2="10" y2="40"/><line x1="38" y1="7" x2="38" y2="40"/></g></svg>Dedicated To Your<br>Business Only</div>
    <div class="cell" style="left:327px;top:245px"><svg width="40" height="40" viewBox="0 0 24 24"><path fill="#4a9fdf" d="M6.6 10.8a15 15 0 006.6 6.6l2.2-2.2c.3-.3.7-.4 1-.2 1.1.4 2.3.6 3.6.6.6 0 1 .4 1 1V20c0 .6-.4 1-1 1A17 17 0 013 4c0-.6.4-1 1-1h3.5c.6 0 1 .4 1 1 0 1.3.2 2.5.6 3.6.1.3 0 .7-.2 1z"/></svg>Dedicated Phone<br>System</div>
    <div class="cell" style="left:654px;top:245px"><svg width="44" height="40" viewBox="0 0 44 40"><path d="M5 28V22a17 17 0 0134 0v6" stroke="#4a9fdf" stroke-width="4" fill="none"/><rect x="2" y="22" width="10" height="16" rx="3" fill="#4a9fdf"/><rect x="32" y="22" width="10" height="16" rx="3" fill="#4a9fdf"/></svg>IT Setup and<br>Support</div>
  </div>
</section>

<section class="contact">
  <div class="abs contact-halo"></div>
  <div class="abs mark" style="top:58px"></div>
  <h2 class="abs section-title" style="top:120px">CONTACT US</h2>
  <div class="abs col-title" style="left:109px;top:188px">Request a Quote</div>
  <div class="abs field" style="left:111px;top:248px;width:297px">Name :</div>
  <div class="abs field" style="left:417px;top:248px;width:296px">Phone no :</div>
  <div class="abs field" style="left:111px;top:310px;width:602px">Email :</div>
  <div class="abs field" style="left:111px;top:371px;width:602px;height:81px">Message :</div>
  <div class="abs submit">SUBMIT</div>

  <div class="abs col-title" style="left:778px;top:188px">Contact Information</div>
  <div class="abs info-row" style="top:243px"><span class="ring"><svg width="14" height="14" viewBox="0 0 24 24"><path fill="#fff" d="M6.6 10.8a15 15 0 006.6 6.6l2.2-2.2c.3-.3.7-.4 1-.2 1.1.4 2.3.6 3.6.6.6 0 1 .4 1 1V20c0 .6-.4 1-1 1A17 17 0 013 4c0-.6.4-1 1-1h3.5c.6 0 1 .4 1 1 0 1.3.2 2.5.6 3.6.1.3 0 .7-.2 1z"/></svg></span>07 3000 4821</div>
  <div class="abs info-row" style="top:308px"><span class="ring"><svg width="15" height="12" viewBox="0 0 15 12"><rect width="15" height="12" rx="1" fill="#fff"/><path d="M0 1l7.5 6L15 1" stroke="#0f1c2e" stroke-width="1.5" fill="none"/></svg></span>info@hire4ward.com.au/</div>
  <div class="abs col-title" style="left:778px;top:370px">Social Media</div>
  <div class="abs" style="left:778px;top:422px;display:flex;gap:12px">
    <span class="ring"></span><span class="ring"></span><span class="ring"></span>
  </div>
</section>

<footer class="site-footer">
  <p class="abs copyright">Copyright © 2020, HIRE 4 WARD. All rights reserved.</p>
  <svg class="abs" style="left:1062px;top:28px" width="28" height="16" viewBox="0 0 28 16"><path d="M2 14L14 3l12 11" stroke="#555" stroke-width="3" fill="none"/></svg>
</footer>

</body>
</html>
```